Business Card Design

I would like a new business card that incorporates the new colors and font of the attached MDP4x10.pdf file of our new sign (latte & luxurious red from Halcott Brennan colors) with the logo from the old business card (file name is New2014.pdf). You can remove the phrases from the old card, and just use the contact info provided above. Please let me know if you have any questions.

Industry/Entity Type

Business

Contact Information for Business Card

Marcus Dean Pryor, LLC
Real Estate Attorney
482 Alder Street
Cedar Hollow, GA 30577
(O) 555-302-4187
(C) 555-719-2630
marcus@mdpcounsel.com
mdpcounsel.com

```html
<!DOCTYPE html>
<html lang="en">
<head>
<meta charset="utf-8">
<title>Marcus Dean Pryor, LLC — Business Card</title>
<link rel="stylesheet" href="https://fonts.googleapis.com/css2?family=Open+Sans:wght@400;700&display=swap">
<style>
  :root {
    --luxurious-red: #b8505f;
    --latte: #f1ebe1;
    --backdrop: #e6e2dc;
    --white: #ffffff;
  }
  * { box-sizing: border-box; margin: 0; padding: 0; }
  html, body {
    width: 1200px; height: 780px; overflow: hidden;
    background: var(--backdrop);
  }
  .stage {
    position: relative; width: 1200px; height: 780px;
    display: flex; align-items: center; justify-content: center;
  }
  .business-card {
    position: relative; width: 1050px; height: 600px;
    background: var(--luxurious-red);
    box-shadow: 0 6px 18px rgba(0,0,0,0.18);
    overflow: hidden;
    font-family: "Open Sans", Arial, sans-serif;
    color: var(--luxurious-red);
  }
  .card-shape { position: absolute; inset: 0; }
  .firm-name {
    position: absolute; left: 400px; top: 120px; width: 480px;
    text-align: center; white-space: nowrap;
    font-weight: 700; font-size: 36px; line-height: 1.2;
    color: var(--luxurious-red);
  }
  .contact-block { position: absolute; left: 205px; top: 300px; }
  .person-name { font-weight: 700; font-size: 42px; line-height: 1.05; }
  .person-title { font-weight: 400; font-size: 22px; margin-bottom: 16px; }
  .contact-list { list-style: none; }
  .contact-item {
    display: flex; align-items: center; gap: 12px;
    font-size: 23px; line-height: 35px;
  }
  .contact-icon { width: 24px; height: 24px; flex: none; }
  .office-address {
    position: absolute; right: 42px; top: 480px;
    text-align: right; color: var(--white); font-style: normal;
    font-size: 24px; line-height: 36px; font-weight: 400;
    white-space: nowrap;
  }
</style>
</head>
<body>
<main class="stage">
  <article class="business-card">
    <svg class="card-shape" viewBox="0 0 1050 600" aria-hidden="true">
      <path fill="var(--latte)" d="M380,0 L900,0 C1010,200 960,450 560,600 L120,600 C60,400 180,150 380,0 Z"/>
    </svg>

    <header class="firm-name">Marcus Dean Pryor, LLC</header>

    <section class="contact-block">
      <h1 class="person-name">Marcus Dean</h1>
      <p class="person-title">Managing Director</p>
      <ul class="contact-list">
        <li class="contact-item">
          <svg class="contact-icon" viewBox="0 0 24 24" aria-label="Office phone">
            <rect width="24" height="24" rx="3" fill="var(--luxurious-red)"/>
            <path d="M5 9 Q12 4 19 9 L17 11 L14 9.5 L10 9.5 L7 11 Z" fill="var(--white)"/>
            <rect x="6" y="12" width="12" height="7" rx="1" fill="var(--white)"/>
          </svg>
          <span>555-302-4187</span>
        </li>
        <li class="contact-item">
          <svg class="contact-icon" viewBox="0 0 24 24" aria-label="Mobile phone">
            <rect width="24" height="24" rx="3" fill="var(--luxurious-red)"/>
            <rect x="8" y="4" width="8" height="16" rx="1.5" fill="var(--white)"/>
            <rect x="9.5" y="6" width="5" height="9" fill="var(--luxurious-red)"/>
          </svg>
          <span>555-719-2630</span>
        </li>
        <li class="contact-item">
          <svg class="contact-icon" viewBox="0 0 24 24" aria-label="Email">
            <rect width="24" height="24" rx="3" fill="var(--luxurious-red)"/>
            <rect x="5" y="7" width="14" height="10" fill="var(--white)"/>
            <path d="M5 7 L12 13 L19 7" fill="none" stroke="var(--luxurious-red)" stroke-width="1.5"/>
          </svg>
          <span>marcus@mdpcounsel.com</span>
        </li>
        <li class="contact-item">
          <svg class="contact-icon" viewBox="0 0 24 24" aria-label="Website">
            <rect width="24" height="24" rx="3" fill="var(--luxurious-red)"/>
            <g fill="none" stroke="var(--white)" stroke-width="1.5">
              <circle cx="12" cy="12" r="7"/>
              <ellipse cx="12" cy="12" rx="3" ry="7"/>
              <path d="M5 12 H19"/>
            </g>
          </svg>
          <span>mdpcounsel.com</span>
        </li>
      </ul>
    </section>

    <address class="office-address">
      482 Alder Street<br>
      Cedar Hollow, GA 30577
    </address>
  </article>
</main>
</body>
</html>
```